Bref créative
Design Business Card & Stationary
Talvix Studio
Professional
Derek Holt
4837 Birchwood Lane Suite #210
Lakemont, CA 91847
derek@talvixstudio.example
www.talvixstudio.example
This is our logo

```html
<!DOCTYPE html>
<html lang="en">
<head>
<meta charset="utf-8">
<title>Talvix Studio – Business Cards</title>
<link rel="stylesheet" href="https://fonts.googleapis.com/css2?family=Source+Sans+3:wght@400;600;700&display=swap">
<style>
  :root {
    --bg: #e9e6e1;
    --card: #ffffff;
    --green: #7cb534;
    --green-dark: #5d9322;
    --ink: #3c3c3c;
    --muted: #6a6a6a;
    --icon: #e4efd4;
  }
  * { margin: 0; padding: 0; box-sizing: border-box; }
  html, body { width: 1200px; height: 852px; overflow: hidden; }
  body {
    background: var(--bg);
    font-family: "Source Sans 3", "Myriad Pro", Arial, sans-serif;
    color: var(--ink);
    position: relative;
  }
  .card {
    position: absolute;
    width: 480px;
    height: 280px;
    background: var(--card);
    border-radius: 18px;
    overflow: hidden;
    box-shadow: 0 6px 18px rgba(0,0,0,.18);
  }
  .card--wide { left: 110px; top: 140px; }
  .card--slim { left: 610px; top: 432px; }

  .band { position: absolute; left: 0; top: 0; height: 100%; }
  .card--wide .band { width: 120px; }
  .card--slim .band { width: 72px; }

  .brand {
    position: absolute;
    display: flex;
    align-items: center;
    gap: 10px;
  }
  .card--wide .brand { left: 92px; top: 30px; }
  .card--slim .brand { left: 46px; top: 34px; }
  .brand-mark {
    width: 52px; height: 52px;
    border-radius: 50%;
    background: var(--green-dark);
    border: 4px solid #fff;
    box-shadow: 0 1px 3px rgba(0,0,0,.2);
  }
  .brand-text { display: flex; flex-direction: column; }
  .brand-name {
    font-size: 34px;
    font-weight: 600;
    color: var(--green-dark);
    line-height: 1;
    letter-spacing: -.5px;
  }
  .brand-tagline {
    font-size: 11px;
    color: var(--muted);
    margin-top: 3px;
    letter-spacing: .3px;
  }

  .address {
    position: absolute;
    font-size: 12px;
    line-height: 1.35;
    color: var(--ink);
  }
  .card--wide .address { left: 140px; top: 118px; }
  .card--slim .address { left: 96px; top: 124px; }

  .holder {
    position: absolute;
    font-size: 17px;
    font-weight: 700;
    color: var(--green);
  }
  .card--wide .holder { right: 40px; top: 128px; }
  .card--slim .holder { right: 40px; top: 138px; }

  .contacts {
    position: absolute;
    list-style: none;
    font-size: 11.5px;
    line-height: 18px;
    color: var(--ink);
  }
  .card--wide .contacts { left: 124px; top: 190px; }
  .card--wide .contacts li { display: flex; align-items: center; gap: 8px; }
  .card--slim .contacts { left: 96px; top: 196px; }

  .glyph { width: 10px; height: 10px; flex: none; }

  .icon-rail {
    position: absolute;
    left: 30px;
    display: flex;
    flex-direction: column;
    gap: 8px;
  }
  .rail-home { top: 150px; }
  .rail-contact { top: 200px; }
  .icon-rail svg { width: 11px; height: 11px; }
</style>
</head>
<body>

<section class="card card--wide">
  <svg class="band" viewBox="0 0 120 280" preserveAspectRatio="none" aria-hidden="true">
    <defs>
      <linearGradient id="bandFillWide" x1="0" y1="0" x2="0" y2="1">
        <stop offset="0" stop-color="#8cc440"/>
        <stop offset="1" stop-color="#6aa52a"/>
      </linearGradient>
    </defs>
    <path d="M0 0 H96 Q112 0 112 20 V250 Q112 280 84 280 H0 Z" fill="url(#bandFillWide)"/>
  </svg>

  <div class="brand">
    <span class="brand-mark"></span>
    <div class="brand-text">
      <span class="brand-name">Talvix Studio</span>
      <span class="brand-tagline">Digital Reach Consulting</span>
    </div>
  </div>

  <p class="address">4837 Birchwood Lane Suite #210<br>Lakemont, CA 91847</p>
  <p class="holder">Derek Holt</p>

  <ul class="contacts">
    <li>
      <svg class="glyph" viewBox="0 0 10 10"><path d="M2 1 L4 1 L4.6 3 L3.4 4 Q4.5 6 6 6.6 L7 5.4 L9 6 L9 8 Q5 9 1 3 Z" fill="var(--green-dark)"/></svg>
      619-555-0142
    </li>
    <li>
      <svg class="glyph" viewBox="0 0 10 10"><rect x="3" y="0.5" width="4.5" height="9" rx="1" fill="var(--green-dark)"/><rect x="3.8" y="1.6" width="2.9" height="5.4" fill="#fff"/></svg>
      619-555-0187
    </li>
    <li>
      <svg class="glyph" viewBox="0 0 10 10"><rect x="0.5" y="2" width="9" height="6" rx="1" fill="var(--green-dark)"/><path d="M1 2.5 L5 5.5 L9 2.5" stroke="#fff" fill="none" stroke-width=".8"/></svg>
      derek@talvixstudio.example
    </li>
    <li>
      <svg class="glyph" viewBox="0 0 10 10"><circle cx="5" cy="5" r="4.5" fill="var(--green-dark)"/><path d="M0.5 5 H9.5 M5 0.5 Q2 5 5 9.5 Q8 5 5 0.5" stroke="#fff" fill="none" stroke-width=".6"/></svg>
      www.talvixstudio.example
    </li>
  </ul>
</section>

<section class="card card--slim">
  <svg class="band" viewBox="0 0 72 280" preserveAspectRatio="none" aria-hidden="true">
    <defs>
      <linearGradient id="bandFillSlim" x1="0" y1="0" x2="0" y2="1">
        <stop offset="0" stop-color="#8cc440"/>
        <stop offset="1" stop-color="#6aa52a"/>
      </linearGradient>
    </defs>
    <rect width="72" height="280" fill="url(#bandFillSlim)"/>
  </svg>

  <div class="brand">
    <span class="brand-mark"></span>
    <div class="brand-text">
      <span class="brand-name">Talvix Studio</span>
      <span class="brand-tagline">Digital Reach Consulting</span>
    </div>
  </div>

  <p class="address">4837 Birchwood Lane Suite #210<br>Lakemont, CA 91847</p>
  <p class="holder">Derek Holt</p>

  <div class="icon-rail rail-home" aria-hidden="true">
    <svg viewBox="0 0 10 10"><path d="M5 1 L9.5 5 H8 V9 H2 V5 H0.5 Z" fill="var(--icon)"/></svg>
  </div>

  <div class="icon-rail rail-contact" aria-hidden="true">
    <svg viewBox="0 0 10 10"><path d="M2 1 L4 1 L4.6 3 L3.4 4 Q4.5 6 6 6.6 L7 5.4 L9 6 L9 8 Q5 9 1 3 Z" fill="var(--icon)"/></svg>
    <svg viewBox="0 0 10 10"><rect x="3" y="0.5" width="4.5" height="9" rx="1" fill="var(--icon)"/></svg>
    <svg viewBox="0 0 10 10"><rect x="0.5" y="2" width="9" height="6" rx="1" fill="var(--icon)"/></svg>
    <svg viewBox="0 0 10 10"><circle cx="5" cy="5" r="4.5" fill="var(--icon)"/></svg>
  </div>

  <ul class="contacts">
    <li>619-555-0142</li>
    <li>619-555-0187</li>
    <li>derek@talvixstudio.example</li>
    <li>www.talvixstudio.example</li>
  </ul>
</section>

</body>
</html>
```